Business card design for Medical Practice Mgmt company
Ashfield Clinic Allies
Business card design for Medical Practice Mgmt company - Medical
Creative Brief
Professional
Monica Daltrey
VP of Operations
4170 E Holloway Ln # 210 Plano, TX 75041
mdaltrey@aca-mail.net
www.ashfieldclinicallies.net
jdovan jdovan
uploaded AI file
bluefern bluefern
Logo Ai file needed!

```html
<!DOCTYPE html>
<html lang="en">
<head>
<meta charset="utf-8">
<title>Ashfield Clinic Allies – Business Card</title>
<link href="https://fonts.googleapis.com/css2?family=Open+Sans:wght@400;600;700&family=Montserrat:wght@500&display=swap" rel="stylesheet">
<style>
  :root {
    --bg: #d9d9db;
    --card-white: #ffffff;
    --brand-blue: #3a80c6;
    --ink: #1c1c1c;
    --name-bar: #000000;
    --on-blue: #ffffff;
    --tagline: #3a80c6;
  }
  * { margin: 0; padding: 0; box-sizing: border-box; }
  html, body { width: 1200px; height: 842px; overflow: hidden; }
  body {
    background: var(--bg);
    font-family: "Open Sans", Arial, sans-serif;
    display: flex;
    align-items: center;
    justify-content: center;
    gap: 60px;
  }
  .card {
    position: relative;
    width: 520px;
    height: 297px;
    overflow: hidden;
    box-shadow: 0 6px 18px rgba(0,0,0,0.18);
  }

  /* Front */
  .card-front { background: var(--card-white); }
  .front-band {
    position: absolute; left: 0; right: 0; top: 138px; height: 136px;
    background: var(--brand-blue);
  }
  .brand-lockup {
    position: absolute; left: 228px; top: 40px;
    display: flex; align-items: center; gap: 10px;
  }
  .brand-dot {
    width: 30px; height: 30px; border-radius: 50%;
    background: var(--brand-blue); flex: none;
  }
  .brand-name {
    font-family: "Montserrat", Arial, sans-serif;
    font-weight: 500; font-size: 23px; color: var(--ink);
    letter-spacing: 0.5px; white-space: nowrap;
  }
  .tagline {
    position: absolute; left: 270px; top: 80px;
    font-size: 7px; color: var(--tagline); letter-spacing: 0.4px;
    text-transform: uppercase;
  }
  .name-bar {
    position: absolute; left: 0; top: 100px; width: 222px; height: 38px;
    background: var(--name-bar); color: var(--on-blue);
    padding: 4px 0 0 14px;
  }
  .person-name { font-size: 13px; font-weight: 700; line-height: 16px; }
  .person-title { font-size: 10px; line-height: 14px; }
  .address {
    position: absolute; left: 14px; top: 150px;
    color: var(--on-blue); font-size: 10.5px; line-height: 15px;
  }
  .divider {
    position: absolute; left: 222px; top: 138px; width: 2px; height: 136px;
    background: var(--card-white);
  }
  .contacts {
    position: absolute; left: 238px; top: 148px;
    list-style: none; color: var(--on-blue); font-size: 10.5px;
  }
  .contacts li { display: flex; align-items: center; gap: 7px; height: 18px; }
  .contacts svg { width: 11px; height: 11px; flex: none; }

  /* Back */
  .card-back { background: var(--brand-blue); }
  .back-mark {
    position: absolute; left: 290px; top: 70px;
    width: 110px; height: 110px; border-radius: 50%;
    background: var(--card-white);
  }
  .back-url {
    position: absolute; left: 0; right: 0; top: 226px; text-align: center;
    color: var(--on-blue); font-size: 12px; letter-spacing: 3px;
  }
</style>
</head>
<body>
  <section class="card card-front">
    <div class="front-band"></div>
    <div class="brand-lockup">
      <span class="brand-dot"></span>
      <span class="brand-name">Ashfield Clinic Allies</span>
    </div>
    <p class="tagline">Practice management for independent physician groups</p>
    <div class="name-bar">
      <p class="person-name">Monica Daltrey</p>
      <p class="person-title">VP of Operations</p>
    </div>
    <p class="address">4170 E Holloway Ln<br># 210 Plano, TX 75041</p>
    <div class="divider"></div>
    <ul class="contacts">
      <li><svg viewBox="0 0 12 12"><circle cx="6" cy="6" r="6" fill="#fff"/><path d="M4 3.2l1 1.2-.6.8c.4.8 1 1.4 1.8 1.8l.8-.6 1.2 1-.6 1.1C5.6 8.3 3.7 6.4 3.2 4z" fill="#3a80c6"/></svg>469-555-0141</li>
      <li><svg viewBox="0 0 12 12"><circle cx="6" cy="6" r="6" fill="#fff"/><rect x="4.2" y="2.6" width="3.6" height="6.8" rx=".6" fill="#3a80c6"/></svg>469-555-0187</li>
      <li><svg viewBox="0 0 12 12"><circle cx="6" cy="6" r="6" fill="#fff"/><rect x="3" y="4.6" width="6" height="3.4" fill="#3a80c6"/><rect x="4" y="3" width="4" height="1.6" fill="#3a80c6"/></svg>469-555-0142</li>
      <li><svg viewBox="0 0 12 12"><circle cx="6" cy="6" r="6" fill="#fff"/><rect x="3" y="3.8" width="6" height="4.4" fill="#3a80c6"/><path d="M3 3.8l3 2.4 3-2.4" stroke="#fff" stroke-width=".7" fill="none"/></svg>mdaltrey@aca-mail.net</li>
      <li><svg viewBox="0 0 12 12"><circle cx="6" cy="6" r="6" fill="#fff"/><circle cx="6" cy="6" r="3.2" fill="none" stroke="#3a80c6" stroke-width=".8"/><path d="M2.8 6h6.4M6 2.8v6.4" stroke="#3a80c6" stroke-width=".7"/></svg>www.ashfieldclinicallies.net</li>
    </ul>
  </section>

  <section class="card card-back">
    <div class="back-mark"></div>
    <p class="back-url">www.ashfieldclinicallies.net</p>
  </section>
</body>
</html>
```